business card for LWR pty ltd

We require a business card that stands out . I have included our company flyer and would like the services listed to be put on the card so when we Give out the cards to customers they have an idea of services we provide. need the winning design to be in editable photo shop format, editable iMac pages format or editable windows publisher format, so that I can enter in names, email addresses, phone numbers etc myself. I have included a pdf documents of info / items needed on the card to use as reference please.
Updates

need more submissions

Need extra days to review

Sick

Target Market(s)

new customers

Contact Information for Business Card

details are on attached business card requirements file

Requirements
Must have
• I have attached a list of must haves

```html
<!DOCTYPE html>
<html lang="en">
<head>
<meta charset="utf-8">
<title>LWR Pty Ltd – Business Card</title>
<link href="https://fonts.googleapis.com/css2?family=Red+Hat+Display:wght@400;500;700;800&display=swap" rel="stylesheet">
<style>
  :root {
    --page-bg: #e4e4e4;
    --card-black: #0d0d0d;
    --card-dark: #1a1a1a;
    --gold: #b8873e;
    --gold-band: #b08440;
    --white: #ffffff;
    --text-soft: #e8e8e8;
    --silver: #b9b9b9;
    --font: "Red Hat Display", Arial, sans-serif;
  }
  * { box-sizing: border-box; margin: 0; padding: 0; }
  html, body { width: 1200px; height: 960px; overflow: hidden; }
  body { background: var(--page-bg); font-family: var(--font); position: relative; }

  .card {
    position: absolute;
    left: 317px;
    width: 568px;
    height: 347px;
    overflow: hidden;
    background: radial-gradient(ellipse at 72% 40%, #2c2c2c 0%, var(--card-dark) 45%, var(--card-black) 100%);
  }
  .card--front { top: 122px; }
  .card--back  { top: 512px; }
  .card svg.card__art { position: absolute; inset: 0; }

  /* Front */
  .contact { position: absolute; left: 46px; top: 38px; color: var(--text-soft); }
  .contact__name { color: var(--gold); font-weight: 700; font-size: 19px; line-height: 22px; }
  .contact__role { font-size: 14px; line-height: 18px; margin-bottom: 17px; }
  .contact__company { color: var(--white); font-weight: 700; font-size: 15px; line-height: 19px; }
  .contact__line { font-size: 14.5px; line-height: 19px; }
  .contact__row { display: flex; align-items: center; gap: 6px; font-size: 14.5px; line-height: 19px; }
  .contact__row--first { margin-top: 5px; }
  .contact__row svg { flex: none; }

  .brand-name {
    position: absolute; left: 268px; top: 62px; width: 272px;
    text-align: center;
    font-weight: 800; font-size: 86px; line-height: 100px; letter-spacing: 4px;
    color: var(--silver);
  }
  .website {
    position: absolute; right: 28px; bottom: 8px;
    color: var(--white); font-weight: 700; font-size: 14px;
  }

  /* Back */
  .services { position: absolute; left: 0; top: 40px; list-style: none; }
  .services li {
    position: relative;
    color: var(--white); font-weight: 700; font-size: 15px; line-height: 19px;
    white-space: nowrap;
  }
  .services li::before {
    content: ""; position: absolute; left: -14px; top: 8px;
    width: 4px; height: 4px; border-radius: 50%; background: var(--gold);
  }
  .services li.services__cont::before { display: none; }

  .callout {
    position: absolute; right: 17px; bottom: 8px;
    color: var(--white); font-size: 13.5px; line-height: 17px; text-align: right;
  }
</style>
</head>
<body>

<section class="card card--front" aria-label="Business card front">
  <svg class="card__art" width="568" height="347" viewBox="0 0 568 347">
    <defs>
      <linearGradient id="front-photo-tone" x1="0" y1="0" x2="0" y2="1">
        <stop offset="0" stop-color="#111" stop-opacity="0"/>
        <stop offset="0.45" stop-color="#2a2a2a"/>
        <stop offset="0.75" stop-color="#8a4f2a"/>
        <stop offset="1" stop-color="#b26a3a"/>
      </linearGradient>
    </defs>
    <rect x="0" y="205" width="568" height="142" fill="url(#front-photo-tone)" role="img" aria-label="Photo of a black road train with three tipper trailers on red outback dirt"/>
    <polygon points="318,317 568,317 568,347 303,347" fill="#1c1c1c"/>
  </svg>

  <div class="contact">
    <p class="contact__name">Daniel Hart</p>
    <p class="contact__role">Director</p>
    <p class="contact__company">LWR Pty Ltd</p>
    <p class="contact__line">Depot: Lot 444 example</p>
    <p class="contact__line">address Australia</p>
    <p class="contact__row contact__row--first">
      <svg width="13" height="13" viewBox="0 0 24 24" aria-hidden="true"><path fill="#b8873e" d="M6.6 10.8a15.1 15.1 0 0 0 6.6 6.6l2.2-2.2a1 1 0 0 1 1-.25 11.4 11.4 0 0 0 3.6.57 1 1 0 0 1 1 1V20a1 1 0 0 1-1 1A17 17 0 0 1 3 4a1 1 0 0 1 1-1h3.5a1 1 0 0 1 1 1c0 1.25.2 2.45.57 3.57a1 1 0 0 1-.25 1z"/></svg>
      000 444 000
    </p>
    <p class="contact__row">
      <svg width="13" height="10" viewBox="0 0 13 10" aria-hidden="true"><rect x="0.75" y="0.75" width="11.5" height="8.5" fill="none" stroke="#b8873e" stroke-width="1.5"/><polyline points="1,1 6.5,5.5 12,1" fill="none" stroke="#b8873e" stroke-width="1.5"/></svg>
      email@lwrservices.com.au
    </p>
  </div>

  <p class="brand-name">LWR</p>
  <p class="website">www.websiteaddress.com</p>
</section>

<section class="card card--back" aria-label="Business card back">
  <svg class="card__art" width="568" height="347" viewBox="0 0 568 347">
    <defs>
      <linearGradient id="back-photo-tone" x1="0" y1="0" x2="0" y2="1">
        <stop offset="0" stop-color="#5d8fc6"/>
        <stop offset="0.35" stop-color="#b9c7d6"/>
        <stop offset="0.65" stop-color="#8e9299"/>
        <stop offset="1" stop-color="#3b3b3d"/>
      </linearGradient>
    </defs>
    <polygon points="0,0 75,0 232,347 0,347" fill="url(#back-photo-tone)" role="img" aria-label="Photo of a white road train prime mover with chrome bull bar under a blue sky"/>
    <polygon points="155,298 568,298 568,347 111,347" fill="var(--gold-band)"/>
  </svg>

  <ul class="services">
    <li style="left:219px">Over Size Loads / Hot Shot Loads</li>
    <li style="left:228px">Heavy Vehicle Recovery Services</li>
    <li style="left:239px">Potable Water Deliveries</li>
    <li style="left:249px">Road Building / Maintenance</li>
    <li style="left:259px">Earthworks</li>
    <li style="left:268px">Sand &amp; Metal Supply &amp; Cartage</li>
    <li style="left:279px">Road Train Tippers</li>
    <li style="left:289px">Road Train Tankers</li>
    <li style="left:299px">Road Train Flat Tops</li>
    <li style="left:309px">Drop Deck Trailers</li>
    <li style="left:320px">Mine Site Accredited</li>
    <li class="services__cont" style="left:330px">Equipment &amp; Operators</li>
  </ul>

  <p class="callout">We offer a large range of services not listed.<br>so call us today for a personalised quote to suit your needs.</p>
</section>

</body>
</html>
```